Tails of Comfort Therapy & Dog Training

I have a dual themed business. I am a nationally recognized dog trainer for NHF (National Hound Federation) and Animal Allies (Pet Therapy). One side of my business card will need to address my pet therapy ministry called "Tails of Comfort Therapy". We visit almost 1,000 people a month bringing emotionally uplifting happy visits for nursing homes, veterans hospitals, hospice care, surgery recovery, school systems, and libraries, etc. In addition to emotionally positive effects, pet therapy also helps with anxiety, mobility, regulating blood pressure, and many more advantages. I've attached 2 graphics that are connected with this ministry; #1 paw print inside ribbon heart, #2 clasping hands sketch. The story behind the clasping hands is that it is an actual picture of my hand holding my mother's hand on her death bed (with a sketch filter used). My mother lived in a different state than I live in, and I had wished she had pet therapy available to her in her last months of life. They would have provided some bright moments to her difficult days. So, I vowed that although I was not able to help my own mother, I could train my own dog to reach out to hundreds of people in the community I live in. I have continued to live up to that vow, and have gone on to become a national trainer for other people who would like to train their pets to do the same thing.SIDE TWO of my business card will be announcing that I am a dog trainer for puppies, basic obedience, pet therapy, ESA (emotional support animals), and service dogs. Additionally, I offer canine body language training, dog agility training, and cognitive training. I have also attached two graphics for this side: #1 NHF logo, #2 Animal Allies Evaluation

Target Market(s)

Industry/Entity Type

Dog Training

Contact Information for Business Card

I'm looking for a designer who is good with color scheme & fonts.
2-sided card
one side for pet therapy
one side for dog training

Logo Text

Tails of ComfortTherapy

Font styles to use
Sans Serif
Decorative

Colors

Designer to choose colors to be used in the design.

Requirements
Must have
• -Contact information: Marla Quince (555) 203-9164
• - Contact information for online: Tails of Comfort Therapy (Facebook, Instagram & Twitter)
• - Graphics for pet therapy: clasping hands
• - Graphics for dog training: NHF Model Neighbor Dog, Animal Allies
• - List of dog training classes I offer: Basic Obedience, NHF Model Neighbor Dog, NHF B.R.I.G.H.T. Pup, Pet Therapy training, ESA (Emotional Support Animal), Service Dog training, Canine Body Language, Dog Agility, Cognitive Training, Dog Trick Training
Nice to have
• appealing graphic for dog training school
• Titles in decorative font (but still easy to read) & detail info in very easy to read font

```html
<!DOCTYPE html>
<html lang="en">
<head>
<meta charset="utf-8">
<title>Marla Quince – Business Card</title>
<link rel="stylesheet" href="https://fonts.googleapis.com/css2?family=Open+Sans:wght@400;600&display=swap">
<style>
  :root {
    --olive: #5b6a2b;
    --orange: #f28c45;
    --orange-deep: #ee7d32;
    --gold: #b8a873;
    --gold-light: #e6c98a;
    --ink: #2e2e2e;
    --white: #ffffff;
    --page: #f1f1f1;
  }
  * { box-sizing: border-box; margin: 0; padding: 0; }
  html, body { width: 1200px; height: 900px; overflow: hidden; }
  body {
    background: var(--page);
    font-family: "Open Sans", Arial, sans-serif;
    color: var(--ink);
    display: flex;
    flex-direction: column;
    align-items: center;
    justify-content: center;
    gap: 20px;
  }
  .card {
    position: relative;
    width: 735px;
    height: 420px;
    background: var(--white);
    overflow: hidden;
    box-shadow: 0 4px 10px rgba(0,0,0,0.25);
  }

  /* Therapy side */
  .card-art { position: absolute; inset: 0; }
  .hands-art {
    position: absolute;
    left: 0; top: 160px;
    width: 225px; height: 260px;
    background: radial-gradient(ellipse at 40% 55%, rgba(205,190,165,0.45), rgba(255,255,255,0) 70%);
  }
  .brand {
    position: absolute;
    left: 42px; top: 40px;
    display: flex; align-items: center; gap: 16px;
  }
  .brand-mark {
    width: 70px; height: 70px; border-radius: 50%;
    background: var(--orange);
  }
  .brand-name {
    font-size: 26px; line-height: 1.2; font-weight: 400;
    color: var(--orange);
  }
  .name-band {
    position: absolute;
    left: 0; top: 182px;
    width: 342px; height: 59px;
    background: var(--orange);
    display: flex; align-items: center;
    padding-left: 42px;
  }
  .name-band h1 {
    font-size: 32px; font-weight: 400; color: var(--white);
    letter-spacing: 0.5px; text-transform: uppercase;
  }
  .phone-line {
    position: absolute; left: 44px; top: 250px;
    display: flex; align-items: center; gap: 10px;
    font-size: 18px;
  }
  .find-us {
    position: absolute; left: 44px; top: 281px;
    font-size: 24px; font-weight: 400; color: var(--orange);
  }
  .social-list { position: absolute; left: 44px; top: 315px; list-style: none; }
  .social-list li {
    display: flex; align-items: center; gap: 10px;
    font-size: 18px; line-height: 25px;
  }
  .social-dot {
    width: 14px; height: 14px; border-radius: 50%;
    border: 1.5px solid #6b6b6b;
  }

  /* Training side */
  .training { background: var(--olive); }
  .training-head {
    position: absolute; top: 30px; width: 100%; text-align: center;
  }
  .training-head h2 { font-size: 27px; font-weight: 400; color: var(--orange); }
  .training-head h2 strong { font-weight: 600; }
  .training-head h2 span { color: var(--gold-light); }
  .training-head p { font-size: 27px; color: var(--white); line-height: 1.2; }
  .class-list {
    position: absolute; top: 148px; list-style: none;
    font-size: 17px; line-height: 25px; color: var(--white);
  }
  .class-list.left { left: 30px; }
  .class-list.right { left: 420px; }
  .class-list li { display: flex; align-items: center; gap: 8px; }
  .class-list li::before {
    content: ""; width: 9px; height: 9px; border-radius: 50%;
    background: var(--orange);
  }
  .badge-strip {
    position: absolute; left: 0; top: 310px; width: 100%; height: 88px;
    background: var(--white);
    display: flex; align-items: center; justify-content: center; gap: 18px;
  }
  .badge {
    width: 64px; height: 64px; border-radius: 50%;
    background: #e8cf3a; border: 5px solid #2f5c9c;
  }
  .partner {
    display: flex; align-items: center; gap: 8px;
    font-size: 20px; font-weight: 600; color: #3a3a3a;
    margin: 0 6px;
  }
  .partner-mark { width: 26px; height: 26px; border-radius: 50%; background: #b0213b; }
  .rule-gold { position: absolute; left: 0; top: 398px; width: 100%; height: 8px; background: var(--gold); }
  .rule-orange { position: absolute; left: 0; top: 406px; width: 100%; height: 14px; background: var(--orange); }
</style>
</head>
<body>

<section class="card therapy">
  <div class="hands-art" role="img" aria-label="Faint sketch of two clasped hands"></div>
  <svg class="card-art" width="735" height="420" viewBox="0 0 735 420">
    <defs>
      <linearGradient id="portraitTone" x1="0" y1="0" x2="1" y2="1">
        <stop offset="0" stop-color="#6f6a3a"/>
        <stop offset="0.45" stop-color="#b9814f"/>
        <stop offset="1" stop-color="#d9cbb8"/>
      </linearGradient>
    </defs>
    <path d="M441 0 Q345 210 478 420 L735 420 L735 0 Z" fill="url(#portraitTone)" role="img" aria-label="Portrait of the trainer seated outdoors with her small white dog"/>
    <path d="M432 0 Q336 210 469 420" fill="none" stroke="var(--gold)" stroke-width="6"/>
  </svg>

  <div class="brand">
    <span class="brand-mark"></span>
    <span class="brand-name">Tails of Comfort<br>Therapy</span>
  </div>

  <div class="name-band"><h1>Marla Quince</h1></div>

  <p class="phone-line">
    <svg width="16" height="16" viewBox="0 0 24 24" aria-hidden="true"><path fill="var(--orange)" d="M6.6 10.8a15 15 0 0 0 6.6 6.6l2.2-2.2a1 1 0 0 1 1-.25 11.4 11.4 0 0 0 3.6.57 1 1 0 0 1 1 1V20a1 1 0 0 1-1 1A17 17 0 0 1 3 4a1 1 0 0 1 1-1h3.5a1 1 0 0 1 1 1c0 1.25.2 2.45.57 3.57a1 1 0 0 1-.25 1z"/></svg>
    (555) 203-9164
  </p>

  <h3 class="find-us">FIND US ON:</h3>
  <ul class="social-list">
    <li><span class="social-dot"></span>\Tails of Comfort Therapy</li>
    <li><span class="social-dot"></span>@Tails of Comfort Therapy</li>
    <li><span class="social-dot"></span>\Tails of Comfort Therapy</li>
  </ul>
</section>

<section class="card training">
  <header class="training-head">
    <h2><strong>MARLA QUINCE</strong> <span>(Dog Trainer)</span></h2>
    <p>(555) 203-9164</p>
  </header>

  <ul class="class-list left">
    <li>Basic Obedience</li>
    <li>NHF Model Neighbor Dog</li>
    <li>NHF B.R.I.G.H.T. Pup</li>
    <li>Canine Body Language</li>
    <li>Pet Therapy training</li>
  </ul>
  <ul class="class-list right">
    <li>Service Dog</li>
    <li>ESA (Emotional Support Animal)</li>
    <li>Cognitive</li>
    <li>Dog Agility</li>
    <li>Dog Trick</li>
  </ul>

  <div class="badge-strip">
    <span class="badge"></span>
    <span class="badge"></span>
    <span class="partner"><span class="partner-mark"></span>Animal Allies</span>
    <span class="badge"></span>
    <span class="badge"></span>
  </div>
  <div class="rule-gold"></div>
  <div class="rule-orange"></div>
</section>

</body>
</html>
```